IT Company based on Biology Business Needs a PowerPoint Design

We need a powerpoint design for a new company called 'Tall FERN'. We develop the machine learning solutions especially focused on deep learning algorithms for biology industry. Our initial product is a vision detection on biological images to help doctors diagnose the symptoms. We would like to see designs that use the color green.

Industry/Entity Type

Biotechnology

Requirements
Nice to have
• Lots of slide templates with company logo's look and feel

```html
<!DOCTYPE html>
<html lang="en">
<head>
<meta charset="utf-8">
<title>Tall FERN – Slide Templates</title>
<link rel="stylesheet" href="https://fonts.googleapis.com/css2?family=Saira+Condensed:wght@300;400&family=Quicksand:wght@400;500&display=swap">
<style>
  :root{
    --green:#7bc242;
    --green-dark:#1f9a3e;
    --green-tint:#b8dc8c;
    --ink:#3a3a3a;
    --muted:#5c5c5c;
    --track:#a7a7a7;
    --stage:#cfcfcf;
    --paper:#ffffff;
  }
  *{box-sizing:border-box;margin:0;padding:0}
  html,body{width:1200px;height:1200px;overflow:hidden;background:var(--stage)}
  body{position:relative;font-family:"Quicksand",sans-serif;color:var(--muted)}
  .slide{position:absolute;width:481px;height:360px;background:var(--paper);box-shadow:4px 6px 8px rgba(0,0,0,.28);overflow:hidden}
  .slide--cover{left:102px;top:44px}
  .slide--contents{left:625px;top:42px;width:485px;height:363px}
  .slide--charts{left:102px;top:428px}
  .slide--article{left:627px;top:428px;width:482px}
  .slide--columns{left:102px;top:812px}
  .slide--closing{left:627px;top:812px;width:482px}

  .brand{position:absolute;display:flex;align-items:center;gap:5px;font-family:"Saira Condensed",sans-serif;font-weight:400;white-space:nowrap;letter-spacing:-.2px}
  .brand__dot{border-radius:50%;background:currentColor;display:block}

  .header{position:absolute;left:0;right:0;top:22px;height:32px;background:var(--green);color:#fff}
  .header__title{position:absolute;left:35px;top:2px;font-family:"Saira Condensed",sans-serif;font-weight:300;font-size:20px;letter-spacing:.3px}
  .header .brand{right:22px;top:8px;font-size:12px;color:#fff}
  .header .brand__dot{width:7px;height:7px}
  .footer-rule{position:absolute;left:0;right:0;bottom:8px;height:4px;background:var(--green-dark)}

  /* cover */
  .cover__brand{left:173px;top:65px;font-size:31px;color:var(--green)}
  .cover__brand .brand__dot{width:20px;height:20px}
  .cover__band{position:absolute;left:0;right:0;top:154px;bottom:0;background:var(--green);color:#fff;text-align:center}
  .cover__title{margin-top:38px;font-family:"Saira Condensed",sans-serif;font-weight:300;font-size:31px;letter-spacing:.5px}
  .cover__sub{margin-top:8px;font-family:"Saira Condensed",sans-serif;font-weight:300;font-size:15px;line-height:16px}

  /* contents */
  .toc{position:absolute;left:42px;top:84px;width:425px;list-style:none}
  .toc li{display:flex;align-items:baseline;height:16px;font-family:"Saira Condensed",sans-serif;font-size:8.5px;color:var(--green)}
  .toc li.sub{padding-left:24px;font-size:6.5px;color:var(--muted)}
  .toc .leader{flex:1;border-bottom:1px dotted currentColor;margin:0 2px;transform:translateY(-2px);max-width:none}
  .toc .fill{width:60px}
  .toc .num{width:62px;text-align:right;color:var(--muted);font-size:7.5px}

  /* charts */
  .chart{position:absolute;top:105px;width:140px}
  .chart svg{position:absolute;left:22px;top:0}
  .chart__pct{position:absolute;font-size:8px;font-weight:500;color:var(--green-dark);letter-spacing:.5px}
  .chart__text{position:absolute;top:107px;left:0;width:112px;font-size:7.4px;line-height:10.6px;letter-spacing:.2px}

  /* article */
  .article__lead{position:absolute;left:35px;top:66px;font-family:"Saira Condensed",sans-serif;font-weight:400;font-size:15px;color:#222}
  .article__cols{position:absolute;left:35px;top:92px;width:423px;column-count:2;column-gap:12px;font-family:"Saira Condensed",sans-serif;font-size:6.6px;line-height:10.7px;text-align:justify;color:#333;height:176px;overflow:hidden}
  .article__cols p{margin-bottom:10.7px}

  /* columns */
  .columns__intro{position:absolute;left:35px;top:74px;width:432px;font-size:7.2px;line-height:10.8px;color:#333}
  .pillar{position:absolute;top:114px;width:135px}
  .pillar__title{height:20px;background:var(--green-tint);color:var(--green-dark);font-size:8px;font-weight:500;letter-spacing:.6px;line-height:20px;padding-left:12px}
  .pillar__text{margin:10px 6px 0;font-size:7.4px;line-height:10.7px;text-align:justify;color:#333;height:192px;overflow:hidden}

  /* closing */
  .closing__brand{left:164px;top:184px;font-size:30px;color:var(--green)}
  .closing__brand .brand__dot{width:20px;height:20px}
  .contact-bar{position:absolute;left:0;right:0;top:282px;height:15px;background:var(--green);display:flex;align-items:center;gap:22px;padding-left:120px;color:#fff;font-family:"Saira Condensed",sans-serif;font-size:6.5px}
  .contact-bar span{display:flex;align-items:center;gap:4px}
  .contact-bar svg{width:7px;height:7px}
</style>
</head>
<body>

<section class="slide slide--cover">
  <div class="brand cover__brand"><span class="brand__dot"></span>TALL FERN</div>
  <div class="cover__band">
    <h1 class="cover__title">CLICK TO ADD TITLE</h1>
    <p class="cover__sub">Lorem ipsum dolor sit amet, consectetur<br>adipisicing elit, sed do eiusmod tempor</p>
  </div>
</section>

<section class="slide slide--contents">
  <header class="header"><h2 class="header__title">CLICK TO ADD TITLE</h2><div class="brand"><span class="brand__dot"></span>TALL FERN</div></header>
  <ol class="toc">
    <li>Lorem Ipsum is simply dummy text <span class="leader"></span><span class="num">1</span></li>
    <li class="sub">a) Of the printing and typesetting industry. Lorem Ipsum has been the try's <span class="leader"></span><span class="num">2</span></li>
    <li class="sub">b) Standard dummy text ever since the 1500s, when an unknown printer <span class="leader"></span><span class="num">2</span></li>
    <li>Lorem Ipsum is simply dummy text is the basic dummy text <span class="leader"></span><span class="num">3</span></li>
    <li class="sub">make a type specimen book. It has survived not only five centuries <span class="leader"></span><span class="num">4</span></li>
    <li class="sub">leap into electronic typesetting, remaining <span class="leader"></span><span class="num">5</span></li>
    <li class="sub">larised in the 1960s with the release of Letraset sheets containing <span class="leader"></span><span class="num">6</span></li>
    <li>Lorem Ipsum is simply dummy text <span class="leader"></span><span class="num">7</span></li>
    <li>Lorem Ipsum is simply dummy textlorem ipsum is <span class="leader"></span><span class="num">7</span></li>
  </ol>
  <div class="footer-rule"></div>
</section>

<section class="slide slide--charts">
  <header class="header"><h2 class="header__title">CLICK TO ADD TITLE</h2><div class="brand"><span class="brand__dot"></span>TALL FERN</div></header>

  <div class="chart" style="left:35px">
    <svg width="90" height="90" viewBox="0 0 90 90" aria-hidden="true">
      <circle cx="45" cy="45" r="38" fill="none" stroke="var(--track)" stroke-width="9"/>
      <circle cx="45" cy="45" r="38" fill="none" stroke="var(--green)" stroke-width="9" stroke-dasharray="160 239" transform="rotate(-70 45 45)"/>
    </svg>
    <span class="chart__pct" style="left:0;top:20px">00%</span>
    <span class="chart__pct" style="left:108px;top:70px">00%</span>
    <p class="chart__text">Lorem Ipsum is simply dummy text of the printing and typesetting industry. Lorem Ipsum has been the industry's standard dummy text ever since the 1500s, when an unknown printer took a galley of type and</p>
  </div>

  <div class="chart" style="left:191px">
    <svg width="90" height="90" viewBox="0 0 90 90" aria-hidden="true">
      <circle cx="45" cy="45" r="38" fill="none" stroke="var(--track)" stroke-width="9"/>
      <circle cx="45" cy="45" r="38" fill="none" stroke="var(--green)" stroke-width="9" stroke-dasharray="160 239" transform="rotate(-70 45 45)"/>
    </svg>
    <span class="chart__pct" style="left:0;top:20px">00%</span>
    <span class="chart__pct" style="left:103px;top:70px">00%</span>
    <p class="chart__text">Lorem Ipsum is simply dummy text of the printing and typesetting industry. Lorem Ipsum has been the industry's standard dummy text ever since the 1500s, when an unknown printer took a galley of type and</p>
  </div>

  <div class="chart" style="left:346px">
    <svg width="90" height="90" viewBox="0 0 90 90" aria-hidden="true">
      <circle cx="45" cy="45" r="38" fill="none" stroke="var(--track)" stroke-width="9"/>
      <circle cx="45" cy="45" r="38" fill="none" stroke="var(--green)" stroke-width="9" stroke-dasharray="160 239" transform="rotate(-70 45 45)"/>
    </svg>
    <span class="chart__pct" style="left:-8px;top:20px">00%</span>
    <span class="chart__pct" style="left:105px;top:70px">00%</span>
    <p class="chart__text">Lorem Ipsum is simply dummy text of the printing and typesetting industry. Lorem Ipsum has been the industry's standard dummy text ever since the 1500s, when an unknown printer took a galley of type and</p>
  </div>

  <div class="footer-rule"></div>
</section>

<section class="slide slide--article">
  <header class="header"><h2 class="header__title">CLICK TO ADD TITLE</h2><div class="brand"><span class="brand__dot"></span>TALL FERN</div></header>
  <h3 class="article__lead">Lorem ipsum dolor sit amet, consectetur adipisicing elit, sed do</h3>
  <div class="article__cols">
    <p>Lorem Ipsum is simply dummy text of the printing and typesetting industry. Lorem Ipsum has been the industry's standard dummy text ever since the 1500s, when an unknown printer took a galley of type and scrambled it to make a type specimen book. It has survived not only five centuries, but also the leap into electronic typesetting, remaining essentially unchanged. It was popularised in the 1960s with the release of Letraset sheets containing Lorem Ipsum passages, and more recently with desktop publishing software including versions of Lorem Ipsum.</p>
    <p>It is a long established fact that a reader will be distracted by the readable content of a page when looking at its layout. The point of using Lorem Ipsum is that it has a more-or-less normal distribution of letters, as opposed to using 'Content here, content here', making it look like readable English. Many desktop publishing packages and web page editors now use Lorem Ipsum as their default model text, and a search for 'lorem ipsum' will uncover many web sites still in their infancy. Vari</p>
    <p>Contrary to popular belief, Lorem Ipsum is not simply random text. It has roots in a piece of classical Latin literature from 45 BC, making it over 2000 years old. A Latin professor looked up one of the more obscure Latin words, consectetur, from a Lorem Ipsum passage, and going through the cites of the word in classical literature, discovered the undoubtable source. Lorem Ipsum comes from sections 1.10.32 and 1.10.33 of "de Finibus Bonorum et Malorum" (The Extremes of Good and Evil) by Cicero, written in 45 BC. This book is a treatise on the theory of ethics, very popular during the Renaissance. The first line of Lorem Ipsum, "Lorem ipsum dolor sit amet..", comes from a line in section 1.10.32.</p>
    <p>The standard chunk of Lorem Ipsum used since the 1500s is reproduced below for those interested. Sections 1.10.32 and 1.10.33 from "de Finibus Bonorum et Malorum" by Cicero are also reproduced in their exact original form, accompanied by English versions from the 1914 translation.</p>
    <p>There are many variations of passages of Lorem Ipsum available, but the majority have suffered alteration in some form, by injected humour, or randomised words which don't look even slightly believable. If you are going to use a passage of Lorem Ipsum, you need to be sure there isn't anything embarrassing hidden in the middle of text. All the Lorem Ipsum generators on the Internet tend to repeat predefined chunks as necessary, making this the</p>
  </div>
  <div class="footer-rule"></div>
</section>

<section class="slide slide--columns">
  <header class="header"><h2 class="header__title">CLICK TO ADD TITLE</h2><div class="brand"><span class="brand__dot"></span>TALL FERN</div></header>
  <p class="columns__intro">Lorem Ipsum is simply dummy text of the printing and typesetting industry. Lorem Ipsum has been the industry's standard dummy text ever since the 1500s, when an unknown printer took a galley of type and scrambled it to make a type specimen book. It has survived not only five centuries, but also the leap into electronic</p>

  <div class="pillar" style="left:35px">
    <h4 class="pillar__title">CLICK TO ADD TITLE</h4>
    <p class="pillar__text">Lorem Ipsum is simply dummy text of the printing and typesetting industry. Lorem Ipsum has been the industry's standard dummy text ever since the 1500s, when an unknown printer took a galley of type and scrambled it to make a type specimen book. It has survived not only five centuries, but also the leap into electronic typesetting, remaining essentially unchanged. It was popularised in the 1960s with the release of L<br>It is a long established fact that a reader will be distracted by</p>
  </div>
  <div class="pillar" style="left:182px">
    <h4 class="pillar__title">CLICK TO ADD TITLE</h4>
    <p class="pillar__text">Lorem Ipsum is simply dummy text of the printing and typesetting industry. Lorem Ipsum has been the industry's standard dummy text ever since the 1500s, when an unknown printer took a galley of type and scrambled it to make a type specimen book. It has survived not only five centuries, but also the leap into electronic typesetting, remaining essentially unchanged. It was popularised in the 1960s with the release of L<br>It is a long established fact that a reader will be distracted by</p>
  </div>
  <div class="pillar" style="left:329px">
    <h4 class="pillar__title">CLICK TO ADD TITLE</h4>
    <p class="pillar__text">Lorem Ipsum is simply dummy text of the printing and typesetting industry. Lorem Ipsum has been the industry's standard dummy text ever since the 1500s, when an unknown printer took a galley of type and scrambled it to make a type specimen book. It has survived not only five centuries, but also the leap into electronic typesetting, remaining essentially unchanged. It was popularised in the 1960s with the release of L<br>It is a long established fact that a reader will be distracted by</p>
  </div>

  <div class="footer-rule"></div>
</section>

<section class="slide slide--closing">
  <div class="brand closing__brand"><span class="brand__dot"></span>TALL FERN</div>
  <div class="contact-bar">
    <span><svg viewBox="0 0 10 10" aria-hidden="true"><circle cx="5" cy="5" r="5" fill="#fff"/><path d="M3 2.5l1 1-.6.8a4 4 0 0 0 2.3 2.3l.8-.6 1 1-.7.8C4.6 7.6 2.4 5.4 2.2 3.2z" fill="var(--green)"/></svg>+0 555.210.7734</span>
    <span><svg viewBox="0 0 10 10" aria-hidden="true"><circle cx="5" cy="5" r="5" fill="#fff"/><rect x="2.5" y="3.3" width="5" height="3.4" fill="none" stroke="var(--green)" stroke-width=".8"/></svg>hello@tallfern.net</span>
    <span><svg viewBox="0 0 10 10" aria-hidden="true"><circle cx="5" cy="5" r="5" fill="#fff"/><circle cx="5" cy="5" r="2.6" fill="none" stroke="var(--green)" stroke-width=".8"/></svg>www.tallfern.net</span>
  </div>
</section>

</body>
</html>
```